Post Card Mailer for QUIK PATH PROSPECTS using new logo

We need a post card designed to send through the USA mail service that will go to new prospective clients.

The post card will introduce me and my new company and try to educate them our on company and services.

The goal is for them to call me or email me so I can have a discussion and try to sell our product.

Our product is a name list of individuals that are looking for consulting / help to determine if they qualify for USA social security benefits and then help to manage the process. We sell this name list to law firms that help these individuals.

Our services are better because we have a better less expensive way to identify people via the internet that want help. Our conversion rate is 15%, so every 100 leads a law firm buys the will obtain 15 customers / clients.

Designer on Logo took alot longer than expected. Also there were two projects that needed to combined into one. Which was done yesterday.

Target Market(s)

Law firms

Font styles to use
Serif
Sans Serif
Script

Colors

Designer to choose colors to be used in the design.

Requirements
Must have
• The size of the mailer should be about 6 by 8 inches.
• Two sides.
• Side 1: With our Logo and key messages we want to communicate.
• Side 2: A space to be used by the USA mail services in lower right, my photo and an introduction by me to our company and why they should buy from my company.
Nice to have
• Images that represent what we do, how we help, and our target market.
Should not have
• Poor taste in images that upset people

```html
<!DOCTYPE html>
<html lang="en">
<head>
<meta charset="utf-8">
<title>Quik Path Prospects – Postcard Mailer</title>
<link href="https://fonts.googleapis.com/css2?family=Oswald:wght@400;500;600;700&family=Open+Sans:ital,wght@0,400;0,600;0,700;1,400&display=swap" rel="stylesheet">
<style>
:root{
  --blue:#1565c0;
  --blue-deep:#0d47a1;
  --blue-mid:#1e6fd0;
  --blue-bright:#2f8cf0;
  --navy:#0a1f4d;
  --ice:#8fd3ff;
  --grey-light:#eceef1;
  --grey-mid:#cfd3d8;
  --ink:#222;
  --page:#e7e8ea;
  --white:#fff;
}
*{box-sizing:border-box;margin:0;padding:0}
html,body{width:991px;height:1200px;overflow:hidden;background:var(--page)}
body{position:relative;font-family:"Open Sans",Arial,sans-serif;color:var(--ink)}
.side-label{position:absolute;top:392px;font-family:"Open Sans",Arial,sans-serif;font-weight:700;font-size:24px;letter-spacing:1px;color:#3a3a3a;width:470px;text-align:center}
.side-label.front{left:18px}
.side-label.back{left:503px}
.card{position:absolute;top:440px;width:470px;height:350px;overflow:hidden;background:var(--white);box-shadow:0 2px 8px rgba(0,0,0,.18)}
.card.front{left:18px}
.card.back{left:503px}
.card svg.layer{position:absolute;left:0;top:0}
.brand{font-family:"Oswald",Arial,sans-serif;font-weight:600;color:var(--blue);letter-spacing:.5px;display:flex;align-items:center;gap:6px}
.brand .mark{width:12px;height:12px;background:var(--blue)}
/* FRONT */
.front .brand{position:absolute;left:22px;top:30px;font-size:21px}
.features{position:absolute;left:10px;top:93px;width:272px;display:grid;grid-template-columns:1fr 1fr;color:var(--white)}
.feature{padding:5px 6px 6px}
.feature:nth-child(odd){border-right:1px dashed rgba(255,255,255,.5)}
.feature:nth-child(-n+2){border-bottom:1px dashed rgba(255,255,255,.5)}
.feature h3{font-family:"Oswald",Arial,sans-serif;font-weight:400;font-size:8.5px;text-transform:uppercase;margin-bottom:3px}
.ticks{list-style:none}
.ticks li{position:relative;padding-left:10px;font-size:6.6px;line-height:1.3;margin-bottom:4px}
.ticks li::before{content:"";position:absolute;left:0;top:1px;width:5px;height:5px;border:1px solid rgba(255,255,255,.85);border-radius:50%}
.ticks li::after{content:"";position:absolute;left:2.2px;top:2.4px;width:1.6px;height:2.6px;border-right:1px solid #fff;border-bottom:1px solid #fff;transform:rotate(45deg)}
.contact-bar{position:absolute;left:0;bottom:0;width:470px;height:32px;display:flex;align-items:center;color:var(--white)}
.phone{display:flex;align-items:center;gap:6px;padding-left:14px;width:228px;font-weight:700;font-size:20px;letter-spacing:.5px}
.bar-divider{width:1px;height:20px;background:rgba(255,255,255,.7);margin-right:10px}
.reach p{display:flex;align-items:center;gap:4px}
.reach .address{font-size:5.6px}
.reach .email{font-weight:700;font-size:10.5px;letter-spacing:.3px}
/* BACK */
.portrait{position:absolute;left:26px;top:33px}
.presenter{position:absolute;left:110px;top:34px;color:var(--white);font-family:"Oswald",Arial,sans-serif}
.presenter .first{font-weight:700;font-size:21px;line-height:1;letter-spacing:.5px}
.presenter .last{font-weight:500;font-size:41px;line-height:1.05}
.presenter .role{font-weight:400;font-size:10.5px;margin-top:2px}
.intro-head{position:absolute;left:0;top:143px;width:249px;text-align:center;color:var(--white);font-family:"Oswald",Arial,sans-serif;font-weight:500;font-size:13.5px;line-height:1.25}
.reasons{position:absolute;left:20px;top:204px;width:222px;list-style:none;color:var(--white)}
.reasons li{position:relative;padding-left:9px;font-style:italic;font-size:6.3px;line-height:1.4;margin-bottom:5px}
.reasons li::before{content:"";position:absolute;left:0;top:3px;width:3.5px;height:3.5px;border-radius:50%;background:var(--white)}
.closing{position:absolute;left:0;top:316px;width:249px;text-align:center;color:var(--white);font-family:"Oswald",Arial,sans-serif;font-size:8.8px;line-height:1.35}
.offer{position:absolute;left:256px;top:0;width:214px;text-align:center}
.back .brand{justify-content:center;font-size:15px;margin-top:22px}
.offer .tagline{font-family:"Oswald",Arial,sans-serif;color:var(--blue);font-size:9.5px;line-height:1.45;margin-top:12px;padding:0 6px}
.offer .cta{display:block;margin:7px auto 0;width:175px;height:17px;border-radius:9px;background:var(--blue);color:var(--white);font-family:"Oswald",Arial,sans-serif;font-weight:500;font-size:10px;line-height:17px;letter-spacing:.5px}
.steps{list-style:none;text-align:left;margin:7px 0 0 24px}
.steps li{position:relative;padding-left:9px;font-style:italic;font-size:6.4px;line-height:1.75;color:#222}
.steps li::before{content:"";position:absolute;left:0;top:4px;width:3.5px;height:3.5px;border-radius:50%;background:var(--blue)}
.mail-area{position:absolute;left:270px;top:183px;width:185px;height:160px;border:1px solid #9aa0a6}
.return{position:absolute;left:6px;top:6px;font-size:5.4px;line-height:1.45;font-style:italic}
.return b{font-style:normal;font-weight:700}
.stamp{position:absolute;right:8px;top:6px;width:48px;height:56px;border:1px solid #9aa0a6;font-size:5.5px;text-align:center;padding-top:22px;line-height:1.3;color:#333}
.rule{position:absolute;left:8px;width:168px;height:1px;background:#b9bec4}
</style>
</head>
<body>

<div class="side-label front">FRONT</div>
<div class="side-label back">BACK</div>

<!-- FRONT SIDE -->
<section class="card front">
  <svg class="layer" width="470" height="350" viewBox="0 0 470 350">
    <defs>
      <linearGradient id="greyTop" x1="0" y1="0" x2="0" y2="1">
        <stop offset="0" stop-color="#f7f8fa"/><stop offset="1" stop-color="#d9dde2"/>
      </linearGradient>
      <linearGradient id="panelBlue" x1="0" y1="0" x2="1" y2="1">
        <stop offset="0" stop-color="#1a70cf"/><stop offset="1" stop-color="#1256ac"/>
      </linearGradient>
    </defs>
    <polygon points="0,0 235,0 281,87 0,87" fill="url(#greyTop)"/>
    <polygon points="0,87 281,87 322,165 297,256 0,256" fill="url(#panelBlue)"/>
    <polygon points="0,256 297,256 280,318 0,318" fill="#ffffff"/>
    <rect x="0" y="318" width="470" height="32" fill="var(--blue)"/>
  </svg>
  <svg class="layer" width="470" height="350" viewBox="0 0 470 350" role="img" aria-label="Glowing digital globe floating above an open hand on a deep blue background">
    <defs>
      <radialGradient id="globeGlow" cx="0.66" cy="0.34" r="0.6">
        <stop offset="0" stop-color="#8fd3ff"/><stop offset=".3" stop-color="#2f8cf0"/><stop offset=".75" stop-color="#0f3a86"/><stop offset="1" stop-color="#0a1f4d"/>
      </radialGradient>
    </defs>
    <polygon points="245,0 470,0 470,318 284,318 328,165" fill="url(#globeGlow)"/>
  </svg>
  <svg class="layer" width="470" height="350" viewBox="0 0 470 350" aria-hidden="true">
    <polyline points="238,-4 325,165 282,322" fill="none" stroke="var(--blue-mid)" stroke-width="9"/>
    <polyline points="245,-4 332,165 289,322" fill="none" stroke="#ffffff" stroke-width="1.5"/>
  </svg>
  <svg class="layer" width="470" height="350" viewBox="0 0 470 350" role="img" aria-label="Two round photos: a caregiver helping an older woman, and a judge's gavel">
    <circle cx="72" cy="270" r="34" fill="#c9b8a8" stroke="#fff" stroke-width="3"/>
    <circle cx="72" cy="270" r="37" fill="none" stroke="var(--blue)" stroke-width="2"/>
    <circle cx="155" cy="270" r="34" fill="#c56a1c" stroke="#fff" stroke-width="3"/>
    <circle cx="155" cy="270" r="37" fill="none" stroke="var(--blue)" stroke-width="2"/>
  </svg>

  <div class="brand"><span class="mark"></span>QUIK PATH PROSPECTS</div>

  <div class="features">
    <div class="feature">
      <h3>Best leads, best price</h3>
      <ul class="ticks">
        <li>Our high conversation rates lowers your client acquisition cost.</li>
        <li>Referrals available.</li>
      </ul>
    </div>
    <div class="feature">
      <h3>High volume, quality leads</h3>
      <ul class="ticks">
        <li>50 years of SSD domain knowledge</li>
        <li>Tested technology capabilities</li>
      </ul>
    </div>
    <div class="feature">
      <h3>Trusted partner</h3>
      <ul class="ticks">
        <li>Reliability, Dependable, Helpful</li>
        <li>Deep business &amp; process acumen</li>
      </ul>
    </div>
    <div class="feature">
      <h3>Easy to use</h3>
      <ul class="ticks">
        <li>Integrate seamlessly into your IT systems.</li>
        <li>Tailored campaigns</li>
      </ul>
    </div>
  </div>

  <div class="contact-bar">
    <div class="phone">
      <svg width="16" height="16" viewBox="0 0 24 24" aria-hidden="true"><path fill="#fff" d="M6.6 10.8a15.1 15.1 0 0 0 6.6 6.6l2.2-2.2c.3-.3.7-.4 1-.2 1.1.4 2.3.6 3.6.6.6 0 1 .4 1 1V20c0 .6-.4 1-1 1A17 17 0 0 1 3 4c0-.6.4-1 1-1h3.5c.6 0 1 .4 1 1 0 1.3.2 2.5.6 3.6.1.3 0 .7-.2 1z"/></svg>
      555-014-2273
    </div>
    <div class="bar-divider"></div>
    <div class="reach">
      <p class="address"><svg width="6" height="7" viewBox="0 0 12 16" aria-hidden="true"><path fill="#fff" d="M6 0a6 6 0 0 0-6 6c0 4.5 6 10 6 10s6-5.5 6-10a6 6 0 0 0-6-6zm0 8.5A2.5 2.5 0 1 1 6 3.5a2.5 2.5 0 0 1 0 5z"/></svg>2150 Larkfield Avenue, Suite 400 Dayton Ohio OH 45402</p>
      <p class="email"><svg width="6" height="6" viewBox="0 0 10 10" aria-hidden="true"><circle cx="5" cy="5" r="4" fill="#fff"/></svg>MARCUS@QUIKPATHPROSPECTS.COM</p>
    </div>
  </div>
</section>

<!-- BACK SIDE -->
<section class="card back">
  <svg class="layer" width="470" height="350" viewBox="0 0 470 350" aria-hidden="true">
    <defs>
      <linearGradient id="backBlue" x1="0" y1="0" x2="0" y2="1">
        <stop offset="0" stop-color="#1565c0"/><stop offset="1" stop-color="#1a6fd3"/>
      </linearGradient>
    </defs>
    <polygon points="0,0 187,0 249,52 249,350 0,350" fill="url(#backBlue)"/>
    <polygon points="0,0 160,0 215,46 215,135 0,135" fill="#1a72d6" opacity=".55"/>
    <polygon points="0,138 249,138 249,188 0,188" fill="var(--blue-deep)" opacity=".55"/>
    <line x1="10" y1="190" x2="240" y2="190" stroke="#fff" stroke-opacity=".35" stroke-width="1"/>
  </svg>
  <svg class="portrait" width="74" height="90" viewBox="0 0 74 90" role="img" aria-label="Portrait photo of Marcus Delwyn">
    <rect x="0" y="0" width="74" height="90" fill="#ffffff"/>
    <rect x="3" y="3" width="68" height="84" fill="#6d7480"/>
  </svg>

  <div class="presenter">
    <div class="first">MARCUS</div>
    <div class="last">DELWYN</div>
    <div class="role">PRESIDENT, QUIK PATH PROSPECTS</div>
  </div>

  <h2 class="intro-head">I WANT TO PERSONALLY INTRODUCE<br>OUR COMPANY TO YOU!</h2>

  <ul class="reasons">
    <li>My team as &gt; 50 years of cumulative SSD experience.</li>
    <li>We have proven technology that delivers the best leads.</li>
    <li>The timing is right for a new competitor in this industry.</li>
    <li>I had to come out of retirement after 30 years with Norvale, the opportunity is just that great … I love building businesses and partnering with great customers!</li>
    <li>Our business, industry, &amp; technical acumen is unrivaled … and we can do it at a cost than no others can.</li>
  </ul>

  <p class="closing">LET'S WORK TOGETHER TO BRING SOCIAL SECURITY<br>DISABILITY BENEFITS TO THOSE IN NEED AND DESERVING!</p>

  <div class="offer">
    <div class="brand"><span class="mark"></span>QUIK PATH PROSPECTS</div>
    <p class="tagline">BEST LEADS. BEST PRICE WITH HIGH VOLUME &amp; QUALITY CAPACITY. LEADS FROM A TRUSTED PARTNER THAT IS EASY TO USE</p>
    <span class="cta">TEST OUR LEADS</span>
    <ul class="steps">
      <li>Start at 250 or 500 Leads.</li>
      <li>Grow to 1,000 … 3,000 or even 10,000!</li>
      <li>We give the right support to your growth.</li>
    </ul>
  </div>

  <div class="mail-area">
    <p class="return"><b>Marcus Delwyn, President Quik Path Prospects</b><br>2150 Larkfield Avenue, Suite 400<br>Dayton Ohio OH 45402<br>555-014-2273<br>Marcus@QuikPathProspects.com</p>
    <div class="stamp">STAMP<br>HERE</div>
    <div class="rule" style="top:76px"></div>
    <div class="rule" style="top:96px"></div>
    <div class="rule" style="top:116px"></div>
    <div class="rule" style="top:136px"></div>
  </div>
</section>

</body>
</html>
```